Wine Label for a Sweet Wine Called "Glimmo"

We need a wine label that will be used for both a sweet red and a sweet white wine. The very important thing to remember is the target market for these wines is: young American women who love sweet wines and they also spend a lot of their money on their hair, clothes, jewelry, nails. They LOVE Glimmo (Glimmo is a word used to describe flashy accessories, jewelry, decoration.) This label needs to be eye catching, showy, fun, glittery. Please put the brand name, "Glimmo," big, and then in smaller but still readable words underneath the label or somewhere on the label: Sweet, Sophisticated, Red (or white). (An example of what I mean is attached). To differentiate between the two color wines you can suggest color changes to differentiate between the red label and the white label but the label design itself should be the same. Ultimately, the label can be the exact same label for both white and red as long as it looks good on a white wine (a greenish/yellow wine in a clear glass bottle) and a red wine (a dark color wine in a dark bottle).

I've attached an example of the text size relationship between the word Glimmo and the words to go underneath or elsewhere on the label, but you can certainly play with this-- it is just a suggestion of the text size relationship, and definitely NOT at all mandatory that you use any of these fonts.

You can pick the size of the label but try to stay within normal wine label sizes, meaning don't go bigger than approx. 3.5 inches wide and 5 inches tall.

Target Market(s)

Young American women who love sweet wines and spend a lot of money on their hair, clothes, jewelry, nails. They love Glimmo (Glimmo is a word that means flashy accessories, jewelry, decoration)

Requirements
Must have
• It needs to be flashy, glittery, fun, eye catching, memorable
Nice to have
• It shouldn't be too too ultra feminine! The target market is strong independent women and we also have men who will buy it too.

```html
<!DOCTYPE html>
<html lang="en">
<head>
<meta charset="utf-8">
<title>Glimmo Wine Labels</title>
<link rel="stylesheet" href="https://fonts.googleapis.com/css2?family=Crimson+Pro:wght@400;600;700&display=swap">
<style>
  :root {
    --page: #ffffff;
    --backdrop: #f5f1cd;
    --pearl-1: #eef0ee;
    --pearl-2: #fdfce6;
    --pearl-3: #e6e8e6;
    --graphite: #555657;
    --graphite-soft: #8a8b8c;
    --silver-1: #c9cbcd;
    --silver-2: #f4f5f6;
    --silver-3: #8f9295;
    --wine-1: #7a1219;
    --wine-2: #a01d28;
    --wine-3: #6a1118;
    --wine-4: #2a0b0d;
    --pearl-ink: #f2f0ee;
  }
  * { box-sizing: border-box; margin: 0; padding: 0; }
  html, body { width: 1200px; height: 1000px; overflow: hidden; background: var(--page); }
  .canvas { position: relative; width: 1200px; height: 1000px; }
  .backdrop {
    position: absolute; left: 47px; top: 33px; width: 1110px; height: 937px;
    background: var(--backdrop);
  }
  .label {
    position: absolute;
    font-family: "Crimson Pro", Georgia, serif;
    text-align: center;
    padding: 6px;
  }
  .label__frame {
    position: absolute; inset: 7px;
    border: 3px solid var(--silver-3);
  }
  .label--white {
    left: 165px; top: 100px; width: 349px; height: 372px;
    background: linear-gradient(90deg, var(--pearl-1) 0%, var(--pearl-2) 35%, var(--pearl-2) 55%, var(--pearl-3) 100%);
    border: 5px solid var(--silver-1);
  }
  .label--red {
    left: 167px; top: 496px; width: 350px; height: 376px;
    background: linear-gradient(90deg, var(--wine-1) 0%, var(--wine-2) 30%, var(--wine-3) 60%, var(--wine-4) 100%);
    border: 2px solid var(--wine-1);
  }
  .label--red .label__frame { border-color: var(--silver-2); border-width: 2px; }
  .flourish {
    position: absolute; left: 40px; width: 268px; height: 54px;
  }
  .label--white .flourish { top: 84px; }
  .label--red .flourish { top: 86px; }
  .brand {
    position: absolute; left: 0; right: 0;
    font-weight: 700; font-size: 80px; letter-spacing: 1px; line-height: 1;
  }
  .label--white .brand { top: 140px; color: var(--graphite); }
  .label--red .brand { top: 146px; color: var(--pearl-ink); }
  .rule {
    position: absolute; left: 58px; width: 232px; height: 0;
    border-top: 1.5px dotted;
  }
  .label--white .rule { border-color: var(--graphite-soft); }
  .label--red .rule { border-color: var(--silver-1); }
  .gem {
    position: absolute; left: 164px; width: 20px; height: 10px;
  }
  .tagline {
    position: absolute; left: 0; right: 0;
    font-size: 14px; font-weight: 600; letter-spacing: 1.2px; line-height: 1;
  }
  .label--white .tagline { top: 248px; color: var(--graphite); }
  .label--red .tagline { top: 250px; color: var(--pearl-ink); }
  .label--white .rule--top { top: 220px; }
  .label--white .rule--bottom { top: 266px; }
  .label--white .gem { top: 216px; }
  .label--red .rule--top { top: 224px; }
  .label--red .rule--bottom { top: 267px; }
  .label--red .gem { top: 220px; }
</style>
</head>
<body>
<main class="canvas">
  <div class="backdrop"></div>

  <section class="label label--white">
    <div class="label__frame"></div>
    <svg class="flourish" role="img" aria-label="Ornate scrollwork crest above the brand name" viewBox="0 0 268 54">
      <rect x="0" y="22" width="268" height="14" rx="7" fill="var(--graphite)" opacity="0.35"/>
      <rect x="104" y="4" width="60" height="40" rx="10" fill="var(--graphite)" opacity="0.45"/>
    </svg>
    <h1 class="brand">GLIMMO</h1>
    <div class="rule rule--top"></div>
    <svg class="gem" role="img" aria-label="Small scroll ornament" viewBox="0 0 20 10">
      <rect x="2" y="1" width="16" height="8" rx="4" fill="var(--graphite)"/>
    </svg>
    <p class="tagline">SWEET RED SOPHISTICATED</p>
    <div class="rule rule--bottom"></div>
  </section>

  <section class="label label--red">
    <div class="label__frame"></div>
    <svg class="flourish" role="img" aria-label="Ornate scrollwork crest above the brand name" viewBox="0 0 268 54">
      <rect x="0" y="22" width="268" height="14" rx="7" fill="var(--pearl-ink)" opacity="0.45"/>
      <rect x="104" y="4" width="60" height="40" rx="10" fill="var(--pearl-ink)" opacity="0.55"/>
    </svg>
    <h1 class="brand">GLIMMO</h1>
    <div class="rule rule--top"></div>
    <svg class="gem" role="img" aria-label="Small scroll ornament" viewBox="0 0 20 10">
      <rect x="2" y="1" width="16" height="8" rx="4" fill="var(--pearl-ink)"/>
    </svg>
    <p class="tagline">SWEET RED SOPHISTICATED</p>
    <div class="rule rule--bottom"></div>
  </section>
</main>
</body>
</html>
```